Restoration Specialist in need of business card designs

One side of the business card is a bathroom ripped out down to the studs with just a sink and toilet and then the other side is the bathroom (same sink and toilet) but put back together. Like a before and after on each side behind our information. Stand out, hard to forget, business cards for my restoration company. I want a unique concept all together.
Must include in no particular order:
our business name "Summit Renewals"
Possible Logo for a restoration company
Owner; Dennis Moravec
410-386-7294
dmoravec@summitrenewalsqx.example
SummitRenewalsQX.example (our company website) BUT I am open to any and all designs and options.

Target Market(s)

Customers, Men in the mitigation, plumbing, electrical, HVAC, Roofing, insurance companies

Industry/Entity Type

Restoration/ construction

Contact Information for Business Card

Must include in no particular order: our business name "Summit Renewals" Owner; Dennis Moravec 410-386-7294 dmoravec@summitrenewalsqx.example SummitRenewalsQX.example (our company website) MAY include a list of our services: Residential~ Emergency Response ~ Board- up~ Complete Restoration

Font styles to use
Serif

Colors
0054AA
0677BA
7BADD7
CADEEF
E8F1F8
F0912C
F2A743
F7CA91
FBE8D2
FDF5EE

Requirements
Must have
• unique, memorable, not something men have seen over and over again,
Nice to have
• eye catching
Should not have
• Been something I could have made by myself

```html
<!DOCTYPE html>
<html lang="en">
<head>
<meta charset="utf-8">
<title>Summit Renewals – Business Card</title>
<link href="https://fonts.googleapis.com/css2?family=Noto+Serif:ital,wght@0,400;0,600;0,700;1,400&display=swap" rel="stylesheet">
<style>
  :root {
    --backdrop: #d8d3ce;
    --card-light: #ecebec;
    --panel-light: #5b6c77;
    --panel-dark: #0a1c2b;
    --accent: #d4551c;
    --accent-soft: #e0773f;
    --text-light: #eef1f3;
    --text-muted: #d9dde0;
    --brand-ink: #c84e17;
  }
  * { box-sizing: border-box; margin: 0; padding: 0; }
  html, body {
    width: 1200px; height: 900px; overflow: hidden;
    background: var(--backdrop);
    font-family: "Noto Serif", Georgia, serif;
  }
  .business-card {
    position: absolute; left: 150px; top: 192px;
    width: 900px; height: 516px;
    border-radius: 22px; overflow: hidden;
    background: var(--card-light);
    box-shadow: 0 14px 40px rgba(40, 30, 20, 0.18);
  }
  .card-art { position: absolute; inset: 0; }
  .contact-block { position: absolute; left: 44px; top: 58px; color: var(--text-light); }
  .owner-name {
    font-weight: 600; font-size: 33px; letter-spacing: 1.5px;
    color: var(--accent-soft); text-transform: uppercase; line-height: 1;
  }
  .owner-title { font-style: italic; font-size: 20px; margin-top: 10px; color: var(--text-muted); }
  .contact-list { list-style: none; margin-top: 22px; }
  .contact-list li {
    display: flex; align-items: center; gap: 12px;
    font-size: 19px; height: 31.5px;
  }
  .contact-list svg { width: 16px; height: 16px; fill: var(--accent-soft); flex: none; }
  .services { position: absolute; left: 42px; top: 276px; }
  .services-heading {
    font-weight: 600; font-size: 22px; letter-spacing: 0.5px;
    color: var(--accent-soft); text-transform: uppercase;
  }
  .service-list { list-style: none; margin-top: 6px; }
  .service-list li {
    display: flex; align-items: center; gap: 10px;
    font-size: 19px; height: 29.5px; color: var(--text-muted);
    text-transform: uppercase;
  }
  .service-list li::before {
    content: ""; width: 11px; height: 11px; flex: none;
    background: var(--accent-soft);
  }
  .brand-mark {
    position: absolute; left: 610px; top: 262px; width: 200px;
    display: flex; flex-direction: column; align-items: center; gap: 14px;
  }
  .brand-square { width: 26px; height: 26px; background: var(--brand-ink); }
  .brand-name {
    font-weight: 700; font-size: 34px; line-height: 1.1; text-align: center;
    color: var(--brand-ink); text-transform: uppercase; letter-spacing: 1px;
  }
</style>
</head>
<body>
  <div class="business-card">
    <svg class="card-art" viewBox="0 0 900 516" width="900" height="516" aria-hidden="true">
      <defs>
        <linearGradient id="panelShade" x1="0" y1="0" x2="1" y2="0">
          <stop offset="0" stop-color="var(--panel-light)"/>
          <stop offset="0.55" stop-color="#1a3142"/>
          <stop offset="1" stop-color="var(--panel-dark)"/>
        </linearGradient>
        <linearGradient id="stripeShade" x1="0" y1="0" x2="0" y2="1">
          <stop offset="0" stop-color="#c9490f"/>
          <stop offset="1" stop-color="#e4834d"/>
        </linearGradient>
      </defs>
      <path d="M0 0 H705 C650 150 480 230 400 360 C370 410 352 460 345 516 H0 Z" fill="url(#panelShade)"/>
      <path d="M728 6 C712 130 600 210 500 290 C430 350 385 420 368 490 C400 410 460 350 540 290 C640 210 715 130 728 6 Z" fill="url(#stripeShade)"/>
    </svg>

    <section class="contact-block">
      <h1 class="owner-name">Dennis Moravec</h1>
      <p class="owner-title">Owner</p>
      <ul class="contact-list">
        <li><svg viewBox="0 0 24 24"><path d="M6.6 10.8a15.1 15.1 0 0 0 6.6 6.6l2.2-2.2a1 1 0 0 1 1-.25 11.4 11.4 0 0 0 3.6.6 1 1 0 0 1 1 1V20a1 1 0 0 1-1 1A17 17 0 0 1 3 4a1 1 0 0 1 1-1h3.5a1 1 0 0 1 1 1c0 1.25.2 2.45.57 3.57a1 1 0 0 1-.25 1z"/></svg>410-386-7294</li>
        <li><svg viewBox="0 0 24 24"><path d="M2 5h20v14H2z M4 7v.5l8 5 8-5V7z" fill-rule="evenodd"/></svg>dmoravec@summitrenewalsqx.example</li>
        <li><svg viewBox="0 0 24 24"><path d="M12 2a10 10 0 1 0 0 20 10 10 0 0 0 0-20zm0 2c.9 1.2 1.6 2.6 2 4h-4c.4-1.4 1.1-2.8 2-4zM4.3 14a8 8 0 0 1 0-4h3.3a16 16 0 0 0 0 4zm.9 2h2.8c.3 1.3.8 2.5 1.4 3.6A8 8 0 0 1 5.2 16zM8 8H5.2a8 8 0 0 1 4.2-3.6C8.8 5.5 8.3 6.7 8 8zm4 12c-.9-1.2-1.6-2.6-2-4h4c-.4 1.4-1.1 2.8-2 4zm2.3-6H9.7a14 14 0 0 1 0-4h4.6a14 14 0 0 1 0 4zm.3 5.6c.6-1.1 1.1-2.3 1.4-3.6h2.8a8 8 0 0 1-4.2 3.6zm1.8-5.6a16 16 0 0 0 0-4h3.3a8 8 0 0 1 0 4z"/></svg>SummitRenewalsQX.example</li>
      </ul>
    </section>

    <section class="services">
      <h2 class="services-heading">Our Service</h2>
      <ul class="service-list">
        <li>Residential</li>
        <li>Emergency Response</li>
        <li>Board-Up</li>
        <li>Storm Protection</li>
        <li>Complete Restoration</li>
      </ul>
    </section>

    <div class="brand-mark">
      <span class="brand-square"></span>
      <p class="brand-name">Summit<br>Renewals</p>
    </div>
  </div>
</body>
</html>
```